TRV Capability Statement Brochure

We need a four or six-page flyer/brochure for our capability statement. This should include all the key written copy and photos/descriptions of the personnel, plus contact addresses in the current capability statement which is attached. We are looking for a modern, professional design that matches our professional approach to our business. Please incorporate our logo into the design.

Target Market(s)

Government departments, shipping companies, port operators, lawyers, export and import businesses, commodity companies.

Industry/Entity Type

Business Consultant

Contact Information for Business Card

Professional, simple to read, uncomplicated.

Font styles to use
Serif
Sans Serif

Colors

Designer to choose colors to be used in the design.

Requirements
Must have
• Company logo
• KEY MESSAGE: Providing independent, expert, confidential and professional services.
• Description of company
• Description and photos of personnel.
• Contact details.
Should not have
• No cliches

```html
<!DOCTYPE html>
<html lang="en">
<head>
<meta charset="utf-8">
<title>TRV Capability Statement Brochure</title>
<link rel="stylesheet" href="https://fonts.googleapis.com/css2?family=Oswald:wght@500;700&family=Open+Sans:wght@400;600;700&display=swap">
<style>
:root{
  --stage:#6b6b6b;
  --paper:#ffffff;
  --navy:#1d4b86;
  --blue:#2a6bb3;
  --band:#2c5c97;
  --sky-top:#2f6fc4;
  --sky-mid:#8cc0ec;
  --sea:#1f8fb8;
  --ink:#3a3a3a;
  --muted:#6b6f76;
  --rule:#d7a21a;
}
*{box-sizing:border-box;margin:0;padding:0}
html,body{width:720px;height:1200px;overflow:hidden}
body{background:var(--stage);font-family:"Open Sans",Arial,sans-serif;color:var(--ink);position:relative}
.spread{position:absolute;left:90px;width:540px;height:382px;display:flex;box-shadow:0 6px 18px rgba(0,0,0,.35)}
.spread-cover{top:21px}
.spread-overview{top:409px}
.spread-team{top:797px}
.page{position:relative;width:270px;height:382px;background:var(--paper);overflow:hidden}
.page-left{border-right:1px solid #e4e4e4}
.heading{font-family:"Oswald",Arial,sans-serif;font-weight:700;text-transform:uppercase;letter-spacing:.3px;color:var(--navy)}
.body-text{font-size:4.6px;line-height:1.55;text-align:justify}
.brand{font-family:"Oswald",Arial,sans-serif;font-weight:700;color:var(--navy);display:flex;align-items:center;gap:4px}
.brand-dot{display:inline-block;border-radius:50%;background:var(--navy)}

/* cover spread */
.contacts{position:absolute;left:22px;top:46px;width:140px}
.contacts .heading{font-size:11px;margin-bottom:6px}
.region{margin-bottom:7px}
.region-name{font-family:"Oswald",Arial,sans-serif;font-weight:500;font-size:7px;color:var(--blue);text-transform:uppercase}
.contact-name{font-size:5px;font-weight:600}
.contact-line{font-size:4.8px;display:flex;align-items:flex-start;gap:3px;line-height:1.5}
.contact-line svg{width:5px;height:5px;flex:none;margin-top:1px}
.sea-photo{position:absolute;left:172px;top:52px;width:368px;height:236px;border-radius:24px 0 0 24px;
  background:linear-gradient(180deg,var(--sky-top) 0%,#5b9be0 22%,var(--sky-mid) 48%,#d9ecf8 52%,var(--sea) 56%,#0f6f9a 100%)}
.cover-brand{position:absolute;left:295px;top:18px;font-size:20px}
.cover-brand .brand-dot{width:9px;height:9px}
.key-message{position:absolute;left:300px;top:82px;width:230px;transform:rotate(-6deg);transform-origin:left top}
.key-message .small{font-family:"Oswald",Arial,sans-serif;font-size:7px;color:var(--navy);text-transform:uppercase}
.key-message .big{font-family:"Oswald",Arial,sans-serif;font-weight:700;font-size:12px;color:#fff;text-transform:uppercase;line-height:1.1}
.key-message .light{font-family:"Oswald",Arial,sans-serif;font-weight:500;font-size:11px;color:var(--navy);text-transform:uppercase}
.back-brand{position:absolute;left:190px;top:300px}
.back-brand .brand{font-size:13px}
.back-brand .brand-dot{width:6px;height:6px}
.back-brand p{font-size:4.4px;line-height:1.5;color:var(--muted);margin-top:2px}
.cover-title{position:absolute;left:300px;top:300px}
.cover-title .heading{font-size:8px}
.cover-title .year{font-family:"Oswald",Arial,sans-serif;font-size:15px;color:var(--blue)}
.cover-web{position:absolute;right:18px;top:305px;font-size:4.6px;color:var(--muted)}

/* overview spread */
.overview-photo{position:absolute;inset:0;background:linear-gradient(160deg,#3f7fc9 0%,#9ec6ea 45%,#5c8fc5 75%,#2f5f9c 100%)}
.overview-panel{position:absolute;left:20px;top:28px;width:232px;height:330px;border-radius:16px;background:rgba(28,78,140,.55);padding:14px 14px}
.overview-panel .heading{color:#fff;font-size:12px;text-align:center;margin-bottom:7px}
.overview-panel .body-text{color:#fff;margin-bottom:4px}
.competencies{position:absolute;left:16px;top:22px;width:240px}
.competencies .heading{font-size:11px}
.competencies .lead{font-size:5.6px;font-weight:700;color:var(--navy);margin-bottom:5px}
.comp-row{display:flex;gap:10px;margin-bottom:6px}
.comp-col{flex:1}
.comp-title{font-family:"Oswald",Arial,sans-serif;font-weight:700;font-size:6.2px;color:var(--navy);text-transform:uppercase;margin-bottom:1px}
.comp-list{list-style:none;font-size:4.6px;line-height:1.5}
.comp-list li::before{content:"• ";color:var(--blue)}

/* team spread */
.portrait{background:linear-gradient(180deg,#b9c3cc,#6f7b86);border-radius:8px}
.team-title{position:absolute;left:18px;top:22px;font-size:11px;width:240px}
.team-intro{position:absolute;left:18px;top:42px;width:236px;display:flex;gap:8px}
.team-intro p{flex:1}
.team-band{position:absolute;left:0;top:112px;width:270px;height:124px;background:var(--band)}
.team-band .heading{position:absolute;left:18px;top:10px;color:#fff;font-size:7.5px}
.team-band .body-text{position:absolute;left:18px;top:26px;width:140px;color:#fff}
.name-tag{position:absolute;font-family:"Oswald",Arial,sans-serif;font-weight:500;font-size:5.6px;text-transform:uppercase;color:var(--navy)}
.name-tag.on-band{color:#fff}
.bio{position:absolute;width:140px}
.accent{border-left:1.2px solid var(--rule);padding-left:5px}
.band-right{position:absolute;left:0;top:262px;width:270px;height:120px;background:var(--band)}
</style>
</head>
<body>

<section class="spread spread-cover">
  <div class="page page-left">
    <div class="contacts">
      <h2 class="heading">Contacts:</h2>
      <div class="region">
        <div class="region-name">Victoria</div>
        <div class="contact-name">Martin Hale</div>
        <div class="contact-line"><svg viewBox="0 0 10 10"><circle cx="5" cy="5" r="5" fill="var(--blue)"/><path d="M3 3h1.5l.6 1.5-.8.6a4 4 0 0 0 1.6 1.6l.6-.8L8 6.5V8A5 5 0 0 1 3 3z" fill="#fff"/></svg>+61 400 210 314</div>
        <div class="contact-line"><svg viewBox="0 0 10 10"><circle cx="5" cy="5" r="5" fill="var(--blue)"/><rect x="2.5" y="3.2" width="5" height="3.6" fill="#fff"/><path d="M2.5 3.2L5 5.3l2.5-2.1" stroke="var(--blue)" stroke-width=".6" fill="none"/></svg>martin@trvadvisory.com</div>
        <div class="contact-name">Lena Ostrow</div>
        <div class="contact-line"><svg viewBox="0 0 10 10"><circle cx="5" cy="5" r="5" fill="var(--blue)"/><path d="M3 3h1.5l.6 1.5-.8.6a4 4 0 0 0 1.6 1.6l.6-.8L8 6.5V8A5 5 0 0 1 3 3z" fill="#fff"/></svg>+61 400 382 906</div>
        <div class="contact-line"><svg viewBox="0 0 10 10"><circle cx="5" cy="5" r="5" fill="var(--blue)"/><rect x="2.5" y="3.2" width="5" height="3.6" fill="#fff"/><path d="M2.5 3.2L5 5.3l2.5-2.1" stroke="var(--blue)" stroke-width=".6" fill="none"/></svg>lena@trvadvisory.com</div>
      </div>
      <div class="region">
        <div class="region-name">New South Wales</div>
        <div class="contact-name">Colin Dray</div>
        <div class="contact-line"><svg viewBox="0 0 10 10"><circle cx="5" cy="5" r="5" fill="var(--blue)"/><path d="M3 3h1.5l.6 1.5-.8.6a4 4 0 0 0 1.6 1.6l.6-.8L8 6.5V8A5 5 0 0 1 3 3z" fill="#fff"/></svg>+61 400 517 228</div>
        <div class="contact-line"><svg viewBox="0 0 10 10"><circle cx="5" cy="5" r="5" fill="var(--blue)"/><rect x="2.5" y="3.2" width="5" height="3.6" fill="#fff"/><path d="M2.5 3.2L5 5.3l2.5-2.1" stroke="var(--blue)" stroke-width=".6" fill="none"/></svg>colin@trvadvisory.com</div>
      </div>
      <div class="region">
        <div class="region-name">Tasmania</div>
        <div class="contact-name">Nathan Ellery</div>
        <div class="contact-line"><svg viewBox="0 0 10 10"><circle cx="5" cy="5" r="5" fill="var(--blue)"/><path d="M3 3h1.5l.6 1.5-.8.6a4 4 0 0 0 1.6 1.6l.6-.8L8 6.5V8A5 5 0 0 1 3 3z" fill="#fff"/></svg>+61 400 649 731</div>
        <div class="contact-line"><svg viewBox="0 0 10 10"><circle cx="5" cy="5" r="5" fill="var(--blue)"/><rect x="2.5" y="3.2" width="5" height="3.6" fill="#fff"/><path d="M2.5 3.2L5 5.3l2.5-2.1" stroke="var(--blue)" stroke-width=".6" fill="none"/></svg>nathan@trvadvisory.com</div>
      </div>
      <div class="region">
        <div class="region-name">Queensland</div>
        <div class="contact-name">Grant Vossen</div>
        <div class="contact-line"><svg viewBox="0 0 10 10"><circle cx="5" cy="5" r="5" fill="var(--blue)"/><path d="M3 3h1.5l.6 1.5-.8.6a4 4 0 0 0 1.6 1.6l.6-.8L8 6.5V8A5 5 0 0 1 3 3z" fill="#fff"/></svg>+61 400 773 145</div>
        <div class="contact-line"><svg viewBox="0 0 10 10"><circle cx="5" cy="5" r="5" fill="var(--blue)"/><rect x="2.5" y="3.2" width="5" height="3.6" fill="#fff"/><path d="M2.5 3.2L5 5.3l2.5-2.1" stroke="var(--blue)" stroke-width=".6" fill="none"/></svg>grant@trvadvisory.com</div>
      </div>
      <div class="region">
        <div class="region-name">Registered Address:</div>
        <div class="contact-line"><svg viewBox="0 0 10 10"><circle cx="5" cy="5" r="5" fill="var(--blue)"/><path d="M3 3h1.5l.6 1.5-.8.6a4 4 0 0 0 1.6 1.6l.6-.8L8 6.5V8A5 5 0 0 1 3 3z" fill="#fff"/></svg>+61 3 9000 4821</div>
        <div class="contact-line"><svg viewBox="0 0 10 10"><circle cx="5" cy="5" r="5" fill="var(--blue)"/><path d="M3 3h1.5l.6 1.5-.8.6a4 4 0 0 0 1.6 1.6l.6-.8L8 6.5V8A5 5 0 0 1 3 3z" fill="#fff"/></svg>+61 3 9000 4822</div>
        <div class="contact-line"><svg viewBox="0 0 10 10"><circle cx="5" cy="5" r="5" fill="var(--blue)"/><rect x="2.5" y="3.2" width="5" height="3.6" fill="#fff"/><path d="M2.5 3.2L5 5.3l2.5-2.1" stroke="var(--blue)" stroke-width=".6" fill="none"/></svg>info@trvadvisory.com</div>
        <div class="contact-line"><svg viewBox="0 0 10 10"><circle cx="5" cy="5" r="5" fill="var(--blue)"/><path d="M5 2a2 2 0 0 1 2 2c0 1.5-2 4-2 4S3 5.5 3 4a2 2 0 0 1 2-2z" fill="#fff"/></svg><span>TRV Marine Advisory Pty Ltd,<br>12 Harbour Lane, Portside,<br>Victoria 3990.</span></div>
      </div>
    </div>
    <div class="back-brand">
      <div class="brand"><span class="brand-dot"></span>TRV</div>
      <p>TRV Marine Advisory Pty Ltd<br>ABN 00 000 000 000</p>
    </div>
  </div>
  <div class="page page-right"></div>
  <div class="sea-photo" role="img" aria-label="Open ocean under a blue sky with white clouds"></div>
  <div class="cover-brand brand"><span class="brand-dot"></span>TRV</div>
  <div class="key-message">
    <div class="small">Providing independent, expert</div>
    <div class="big">Confidential &amp; Professional</div>
    <div class="light">Services</div>
  </div>
  <div class="cover-title">
    <div class="heading">Capability Statement</div>
    <div class="year">2017</div>
  </div>
  <div class="cover-web">www.trvadvisory.com</div>
</section>

<section class="spread spread-overview">
  <div class="page page-left">
    <div class="overview-photo" role="img" aria-label="Bulk carrier at sea in soft blue tones"></div>
    <div class="overview-panel">
      <h2 class="heading">Company Overview</h2>
      <p class="body-text">Established in 2009, TRV Marine Advisory has offices in Victoria, New South Wales, Queensland and Tasmania and aims to position itself as a leading maritime consultancy in the region.</p>
      <p class="body-text">The TRV team brings together extensive commercial experience and expertise to offer a highly focused approach to any technical or operational challenge, with analytical insight tailored to each client across the shipping and port industry of the Pacific Rim.</p>
      <p class="body-text">TRV has an international network of associates, including strategic partnerships with global ports and shipping analysts, and membership of respected industry bodies, giving clients access to current market intelligence.</p>
      <p class="body-text">TRV provides shipping, transportation and marine industry expertise to support clients' requirements and strategies. We provide independent, confidential and professional advice through highly experienced and qualified consultants who work closely with clients to understand their needs and deliver results on time and on budget.</p>
      <p class="body-text">TRV is able to step in to a client's existing organisation and supply the skill, knowledge and experience required to support an existing marine operation or port project. We can also apply our expertise to support the preparation of a submission to a tribunal or legal process.</p>
      <p class="body-text">You can count on our professional team to expertly cater to all of your commercial maritime needs. With management experience at the highest levels and extensive technical knowledge, our team is unrivalled in delivering dependable, efficient and cost effective solutions for your business.</p>
    </div>
  </div>
  <div class="page page-right">
    <div class="competencies">
      <h2 class="heading">Core Competencies</h2>
      <p class="lead">TRV has demonstrable experience in the following areas:</p>
      <div class="comp-row">
        <div class="comp-col">
          <div class="comp-title">Commercial Maritime Trade</div>
          <ul class="comp-list">
            <li>Operational knowledge of all major shipping trades</li>
            <li>Thorough understanding of maritime, ports and logistics policy</li>
            <li>Reviews of commercial maritime operations</li>
            <li>Evaluation and management of tenders and proposal preparation</li>
            <li>Feasibility studies (commercial &amp; operational)</li>
          </ul>
        </div>
        <div class="comp-col">
          <ul class="comp-list">
            <li>Advice on joint venture issues and the development of joint venture contracts</li>
            <li>Fleet, availability and trade sector forecasting</li>
            <li>Industry education and training</li>
            <li>Topical industry workshops</li>
            <li>Expert witness</li>
          </ul>
        </div>
      </div>
      <div class="comp-row">
        <div class="comp-col">
          <div class="comp-title">Ship Management</div>
          <ul class="comp-list">
            <li>Vessel ownership and management</li>
            <li>Vessel chartering and operational management</li>
            <li>Vessel sales and purchase</li>
            <li>Advice regarding charter parties</li>
            <li>Re-engineering of marine departments</li>
            <li>Innovative improvements to marine systems</li>
          </ul>
        </div>
        <div class="comp-col">
          <ul class="comp-list">
            <li>Management of suppliers and related resource management</li>
            <li>Managing the shipping requirements of companies</li>
            <li>Analysing and meeting ship charterers' needs from acquisition to cargo delivery into store at the port interface</li>
          </ul>
        </div>
      </div>
      <div class="comp-row">
        <div class="comp-col">
          <div class="comp-title">Ports &amp; Related Industry</div>
          <ul class="comp-list">
            <li>Modelling and optimisation of port throughputs</li>
            <li>Modelling port infrastructure to commodity types and volumes</li>
            <li>Management of port loading and unloading terminals</li>
            <li>Planning and management of the ship/port interface</li>
            <li>Port efficiency assessments</li>
            <li>Modelling port use using queue theory</li>
          </ul>
        </div>
        <div class="comp-col">
          <ul class="comp-list">
            <li>Modelling and forecasting aggregate annual demurrage charges</li>
            <li>Assessments of port and marine safety and security</li>
            <li>Risk assessments of marine and port operations</li>
            <li>Reviews and assessments of navigation and marine safety</li>
            <li>Emergency and crisis management</li>
          </ul>
        </div>
      </div>
      <div class="comp-row">
        <div class="comp-col">
          <div class="comp-title">Supply Chain</div>
          <ul class="comp-list">
            <li>Supply chain evaluation and optimisation</li>
            <li>Evaluation and management of tenders and proposal preparation</li>
            <li>Marine project management, project services and support</li>
          </ul>
        </div>
        <div class="comp-col">
          <ul class="comp-list">
            <li>Management of bulk and breakbulk logistics</li>
            <li>Stacking analysis for bulk terminals</li>
            <li>Re-engineering of supply chains</li>
          </ul>
        </div>
      </div>
    </div>
  </div>
</section>

<section class="spread spread-team">
  <div class="page page-left">
    <h2 class="heading team-title">TRV Marine Advisory Team</h2>
    <div class="team-intro">
      <p class="body-text">All team members have decades of senior-level industry experience in commercial shipping and port operations. The team offers relevant specialist expertise with first-class credentials and the ability to bring together the diverse backgrounds of our people.</p>
      <p class="body-text">Our work spans comprehensive evidence-based analysis and evaluation of major maritime and port projects. We are able to provide innovative solutions to operational problems, financial evaluation of alternatives and board-level proposals for change.</p>
    </div>
    <div class="team-band">
      <h3 class="heading">The TRV Management Team Comprises:</h3>
      <p class="body-text">Based in Sydney, Colin was Master of a fleet of bulk carriers before moving ashore into senior chartering and operational roles. He has held management positions with ship owners and port operators, and served as a director of several industry groups. He also sat on a national marine safety panel for seven years.</p>
      <div class="portrait" role="img" aria-label="Portrait photo of Colin Dray" style="position:absolute;left:170px;top:34px;width:84px;height:78px"></div>
      <div class="name-tag on-band" style="left:180px;top:24px">Colin Dray</div>
    </div>
    <div class="name-tag" style="left:22px;top:248px">Lena Ostrow</div>
    <div class="portrait" role="img" aria-label="Portrait photo of Lena Ostrow" style="position:absolute;left:18px;top:258px;width:84px;height:82px"></div>
    <p class="body-text bio" style="left:112px;top:246px">Based in Melbourne, Lena has more than 40 years of experience in the international maritime and transport industry. She spent several years at sea as a deck officer before taking senior commercial roles ashore. As a leading industry analyst she has been contracted to government agencies, ports and commodity companies across the Pacific Rim, and has written widely on port development. Her work has been recognised by her peers across the industry.</p>
  </div>
  <div class="page page-right">
    <div class="name-tag" style="left:40px;top:18px">Martin Hale</div>
    <div class="portrait" role="img" aria-label="Portrait photo of Martin Hale" style="position:absolute;left:20px;top:28px;width:90px;height:78px"></div>
    <p class="body-text bio accent" style="left:118px;top:16px">Based in Melbourne, Martin is a Master Mariner and holds an MBA. He has over 40 years of experience in the shipping industry. A founding director of TRV, Martin was previously general manager of a major shipping line and led strategic development for a global resources company. He has been closely involved with port and infrastructure projects both within Australia and overseas.</p>
    <p class="body-text bio" style="left:20px;top:120px;width:130px">Based in Hobart, Nathan commenced his maritime career as a deck officer, gaining a broad range of experience in tankers and bulk carriers. He has worked ashore in operational and technical management roles, leading safety and quality systems for a number of vessel operators. Nathan holds recognised qualifications in safety management and auditing.</p>
    <div class="name-tag" style="left:190px;top:112px">Nathan Ellery</div>
    <div class="portrait" role="img" aria-label="Portrait photo of Nathan Ellery" style="position:absolute;left:158px;top:122px;width:92px;height:80px"></div>
    <div class="band-right">
      <div class="name-tag" style="left:28px;top:-10px">Grant Vossen</div>
      <div class="portrait" role="img" aria-label="Portrait photo of Grant Vossen" style="position:absolute;left:20px;top:0;width:92px;height:80px"></div>
      <p class="body-text bio accent" style="left:120px;top:6px;color:#fff">Based in Brisbane, Grant has a seafaring background and over 40 years of commercial shipping experience. A qualified shipbroker, he is a founding shareholder of TRV and has operated liner and tramp services throughout the South Pacific. As principal of a chartering business he brings a wealth of knowledge in ship sale and purchase.</p>
    </div>
  </div>
</section>

</body>
</html>
```